Need a webinar banner promo to place on social media

We are organise a series of webinars in coming months.

We need a webinar banner design to be posted on Facebook and linkedin. The banner is for our webinar titled: Ways to Debut a Novel with Sparkle and Flair.

our website is www.quillmarket.com.au

there is a link on the website to the webinar registration for your reference.

```html
<!DOCTYPE html>
<html lang="en">
<head>
<meta charset="utf-8">
<title>Ways to Debut a Novel with Sparkle and Flair – Webinar Banner</title>
<link rel="stylesheet" href="https://fonts.googleapis.com/css2?family=Red+Hat+Display:wght@300;400;700;900&display=swap">
<style>
  :root {
    --page: #ffffff;
    --navy-deep: #02122a;
    --navy-mid: #0a2d63;
    --navy-glow: #0f4690;
    --gold-dark: #b8862e;
    --gold-light: #f4e27c;
    --gold-flat: #d9b55a;
  }
  * { margin: 0; padding: 0; box-sizing: border-box; }
  html, body {
    width: 1200px;
    height: 1000px;
    overflow: hidden;
    background: var(--page);
  }
  .canvas {
    position: relative;
    width: 1200px;
    height: 1000px;
  }
  .banner {
    position: absolute;
    left: 109px;
    top: 243px;
    width: 982px;
    height: 515px;
    background: radial-gradient(ellipse 60% 75% at 50% 45%, var(--navy-glow) 0%, var(--navy-mid) 45%, var(--navy-deep) 100%);
    overflow: hidden;
  }
  .frame {
    position: absolute;
    left: 55px;
    top: 54px;
    width: 872px;
    height: 405px;
    border-left: 3px solid var(--gold-dark);
    border-right: 3px solid var(--gold-dark);
    border-bottom: 3px solid var(--gold-dark);
  }
  .frame-top {
    position: absolute;
    left: -3px;
    right: -3px;
    top: -1.5px;
    display: flex;
    align-items: center;
    gap: 14px;
  }
  .frame-top .rule {
    flex: 1;
    height: 3px;
    background: linear-gradient(90deg, var(--gold-dark), var(--gold-light), var(--gold-dark));
  }
  .brand {
    display: flex;
    align-items: center;
    gap: 10px;
    transform: translateY(-1px);
  }
  .brand-mark {
    width: 18px;
    height: 18px;
    background: var(--gold-flat);
  }
  .brand-name {
    font-family: "Red Hat Display", sans-serif;
    font-weight: 700;
    font-size: 30px;
    letter-spacing: 2px;
    color: var(--gold-flat);
    line-height: 1;
  }
  .headline {
    position: absolute;
    left: 0;
    right: 0;
    top: 140px;
    text-align: center;
    font-family: "Red Hat Display", sans-serif;
    font-size: 84px;
    line-height: 75px;
    letter-spacing: -2px;
  }
  .headline .line { display: block; }
  .headline span {
    background: linear-gradient(180deg, var(--gold-dark) 15%, var(--gold-light) 85%);
    -webkit-background-clip: text;
    background-clip: text;
    color: transparent;
  }
  .headline .strong { font-weight: 900; }
  .headline .light { font-weight: 300; letter-spacing: 0; }
</style>
</head>
<body>
  <div class="canvas">
    <section class="banner" aria-label="Webinar banner">
      <div class="frame">
        <div class="frame-top">
          <div class="rule"></div>
          <div class="brand">
            <div class="brand-mark"></div>
            <div class="brand-name">QUILL MARKET</div>
          </div>
          <div class="rule"></div>
        </div>
      </div>
      <h1 class="headline">
        <span class="line"><span class="strong">Ways</span> <span class="light">to</span> <span class="strong">Debut</span></span>
        <span class="line"><span class="light">a</span> <span class="strong">Novel</span> <span class="light">with</span></span>
        <span class="line"><span class="strong">Sparkle</span> <span class="light">and</span> <span class="strong">Flair</span></span>
      </h1>
    </section>
  </div>
</body>
</html>
```